Vantor Health Group Presentation Folder, for Cancer Awareness, VERY COLORFUL AND MODERN

Presentation Folder I know pretty much what i want so it should be very eazy , I have included files from folders I use now rebrand them to my new company they will be fine, no sense re creating the wheel
Full Bleed Size
20.87" x 16.68"
53 x 42.4 cm
6260 x 5004 pixels
Document Trim Size
20.75" x 16.56"
52.7 x 42.1 cm
6225 x 4969 pixels
Updates

Low design quality

Industry/Entity Type

Medical

Font styles to use
Serif

Colors

Designer to choose colors to be used in the design.

Requirements
Must have
• really I am not looking for some one to redesign, we like our folder front page and would like to see new word information added., there are two folder front pages to choose from
• So Keep the original front page and redesign the back page and the pockets
• Can Make your Design off of one of the ones I already uploaded
Nice to have
• Keep the same color schemes, Keep the original front page and redesign the back page and the pockets
Should not have
• DO not recreate the front covers, use what I gave you and just rebrand

```html
<!DOCTYPE html>
<html lang="en">
<head>
<meta charset="utf-8">
<title>Vantor Health Group – Hereditary Cancer Screening Folder</title>
<link href="https://fonts.googleapis.com/css2?family=Cinzel:wght@400;600&family=Merriweather:wght@400;700&display=swap" rel="stylesheet">
<style>
  :root{
    --backdrop:#3b3b3d;
    --paper:#f5f5f6;
    --paper-edge:#e4e4e6;
    --frame:#5cc6e8;
    --crimson:#c8173d;
    --ink:#1f1f1f;
    --ink-soft:#444;
    --pink:#e77be6;
    --blue:#3fb6ee;
    --violet:#9a2b8f;
    --logo-blue:#2b4a8c;
  }
  *{box-sizing:border-box;margin:0;padding:0}
  html,body{width:1200px;height:823px;overflow:hidden;background:var(--backdrop)}
  .canvas{position:relative;width:1200px;height:823px}
  .spread{position:absolute;left:124px;top:31px;width:952px;height:760px;display:flex;box-shadow:0 10px 30px rgba(0,0,0,.45)}
  .panel{position:relative;width:476px;height:760px;background:var(--paper)}
  .panel--back{border-right:1px solid var(--paper-edge)}
  .photo{position:absolute;border:3px solid var(--frame);border-radius:12px;overflow:hidden}
  .photo--family-sofa{left:28px;top:88px;width:205px;height:125px;background:linear-gradient(135deg,#efe2d4 0%,#d9a98c 55%,#9a735c 100%)}
  .photo--group-field{left:242px;top:58px;width:208px;height:122px;background:linear-gradient(180deg,#cfe9f1 0%,#d8eef3 45%,#6a9bc8 60%,#5a8f3a 100%)}
  .photo--three-generations{left:28px;top:222px;width:132px;height:96px;background:linear-gradient(135deg,#efe6dc,#c9a58d)}
  .photo--family-meal{left:168px;top:200px;width:130px;height:100px;background:linear-gradient(160deg,#f2f2ef,#c9b28f 70%,#8a6a4a)}
  .photo--beach-walk{left:306px;top:188px;width:144px;height:112px;background:linear-gradient(180deg,#b9c3d6,#e0e1e4 60%,#a9a196)}
  .photo--family-lawn{left:58px;top:306px;width:392px;height:160px;background:linear-gradient(180deg,#9dc56a 0%,#cfe2a4 35%,#e8c9b0 60%,#6e9c3b 100%)}
  .copy{position:absolute;left:30px;top:486px;width:420px;font-family:"Merriweather",serif;color:var(--ink)}
  .copy__intro{font-size:9.5px;line-height:1.55;color:var(--ink-soft)}
  .copy__intro strong{color:var(--ink)}
  .copy__quote{margin-top:12px;font-size:13.5px;font-weight:700;line-height:1.45}
  .cover__title{position:absolute;left:30px;top:46px;width:420px;text-align:center;font-family:"Cinzel",serif;font-weight:600;font-size:22px;color:var(--crimson);letter-spacing:.5px}
  .cover__subtitle{position:absolute;left:30px;top:78px;width:420px;text-align:center;font-family:"Cinzel",serif;font-size:13.5px;color:var(--ink)}
  .cover__lead{position:absolute;left:40px;top:98px;width:400px;text-align:center;font-family:"Merriweather",serif;font-size:6.5px;line-height:1.4;color:var(--ink-soft)}
  .ribbon{position:absolute;left:100px;top:150px;width:300px;height:420px;
    background:radial-gradient(closest-side,rgba(231,123,230,.75) 0%,rgba(154,120,230,.55) 40%,rgba(63,182,238,.45) 70%,rgba(245,245,246,0) 100%)}
  .brand{position:absolute;left:42px;top:640px;display:flex;align-items:center;gap:10px}
  .brand__mark{width:46px;height:46px;border-radius:50%;border:2px solid var(--logo-blue)}
  .brand__name{font-family:"Cinzel",serif;font-size:11px;color:var(--logo-blue);width:90px;line-height:1.2}
  .cover__tagline{position:absolute;left:170px;top:656px;width:290px;text-align:right;white-space:nowrap;font-family:"Cinzel",serif;font-size:13px;color:var(--ink)}
</style>
</head>
<body>
<div class="canvas">
  <div class="spread">
    <section class="panel panel--back">
      <div class="photo photo--family-sofa" role="img" aria-label="Photo: multi-generation family smiling together on a sofa"></div>
      <div class="photo photo--group-field" role="img" aria-label="Photo: large group of people in colourful shirts on a lawn"></div>
      <div class="photo photo--three-generations" role="img" aria-label="Photo: three generations of a family posing together"></div>
      <div class="photo photo--family-meal" role="img" aria-label="Photo: family sharing a meal at a table"></div>
      <div class="photo photo--beach-walk" role="img" aria-label="Photo: family holding hands walking outdoors"></div>
      <div class="photo photo--family-lawn" role="img" aria-label="Photo: happy family lying on the grass in a park"></div>
      <div class="copy">
        <p class="copy__intro"><strong>Hereditary cancer screening</strong> provides vital information to help people with a strong personal or family history of cancer understand their own risk of developing the disease. With this information, they can take steps to Potentially Prevent Cancer, Delay the Onset of Cancer or Catch it at an Earlier stage when outcomes and survival rates are Better.</p>
        <p class="copy__quote">Don't be Afraid of the Answer: Knowledge is Power and Power Eradicates Fear. When You are Fearless, You Will Make all the Right Choices!</p>
      </div>
    </section>
    <section class="panel panel--cover">
      <h1 class="cover__title">Hereditary Cancer Screening</h1>
      <h2 class="cover__subtitle">Doctors are the Gatekeepers to Genetic Testing</h2>
      <p class="cover__lead">We have an obligation to help patients understand genetic risk and how testing can guide heath care decisions</p>
      <div class="ribbon" role="img" aria-label="Illustration: pink and blue awareness ribbon"></div>
      <div class="brand">
        <span class="brand__mark"></span>
        <span class="brand__name">Vantor Health Group</span>
      </div>
      <p class="cover__tagline">The test you order FOR your patients</p>
    </section>
  </div>
</div>
</body>
</html>
```